Postcard designed to acquire new customers

Need a postcard style AD to place in dentist offices and other professionals to promote our tax saving system. We will place these in dentists offices, orthodontist, optometrist, physiotherapist and all sorts of medical/dental offices. The card should highlight how they can save taxes by using our software. Our website has good information on it, and I'll include the advertising PDF that our software company produces. Our logo is a little out-dated and I've included the bonus of the winner re-making the logo so its better than it currently is.
Updates

I don't need to have any space allocated for a stamp and address. We are using this to place in offices and are for advertising purposes, not mailing. Thanks!

Reason: My apologies for not providing feedback yet, I've lost several days due to some illness and am finally back at work. I'll be going through designs today and would like the extra few days to work with many of you to create a great design. Thank you for your patience! Doyle

Reason: Again, my apologies for the delay. I will be in contact with designers this week. Thank you,

Target Market(s)

Small Business Owners in Canada

Industry/Entity Type

Health Insurance

Logo Text

Save Time, Save Money

Font styles to use
Other font styles liked:
• Easy to Read Font's

Colors

Designer to choose colors to be used in the design.

Requirements
Must have
• Must have a call to action on the postcard to sell the service. We need people to have their attention caught. A call to action could be, "You're spending too much on taxes! That's what they'll say if your business doesn't have a 789 Brookvale Outlay Plan..."
• See the PDF for other catch phrases or key information on what a Health Spending Account is. Many people don't know so I'd like to see 3-4 bullet points on the front of the postcard on what a health spending account is. See the attached PDF for that information and simplifying the information to short bullet points would be best. Here are my thoughts:
• Who should have a 789 Brookvale Outlay Plan?
• - Every business owner who is incorporated should have one.
• - Write off 100% of this QTB approved this method.
• - It is the most tax effective way to run dental, health, vision and other expenses through your company.
• - Easy to use APP for your phone, 2-day turnaround time for claims
• If you aren't using this, you're throwing tax dollars away!
• The back of the postcard would include 2 things. First, an example of the taxes you can save, and second - the different information they can send us so we can setup your account.
• First is the example of how this saves you money. Assuming a 38% personal tax rate. You will need to earn $1.62 of gross income, pay $0.62 of personal tax, which leaves you with $1.00 of after tax money to use for your personal expenses.
• The example of using a 789 Brookvale Outlay Plan, or doing nothing would need the following information.
• Comparison
• $5,000 of medical, dental, vision expenses
• Do Nothing 789 Brookvale Outlay Plan
• $8,100 – Total Cost $5,525 – Total Cost
• $3,100 – Income Tax $500 fee & $25 GST
• $5,000 – Money needed for medical, dental, vision, etc. $5,000 – Money needed for medical, dental, vision, etc.
• SAVINGS is $2,575
• Assuming a company incorporated in Alberta and a one time setup fee of $275 has not been included in the comparison.
• Information to send us to setup your account is:
• - Names and birth dates of you and your dependents
• - Contact information for you and your business (if different) Address, email, phone numbers
• - We will contact you about how to setup the app, your banking details and some other items.
• - Setup fee is a one-time payment of $275
Nice to have
• I'd like the front of the postcard to not be very busy with the background or graphics, etc. I want the call to action to be very obvious so they want to read the bullet points and look at the back of the postcard for more information.

```html
<!DOCTYPE html>
<html lang="en">
<head>
<meta charset="utf-8">
<title>789 Brookvale Outlay Plan – Postcard</title>
<link href="https://fonts.googleapis.com/css2?family=Roboto:wght@400;500;700&family=Roboto+Condensed:wght@400;700&family=Oswald:wght@500&display=swap" rel="stylesheet">
<style>
  :root{
    --blue:#1a73c2;
    --orange:#f7941d;
    --dark:#2b2b2b;
    --ink:#222;
    --paper:#fff;
    --stage:#e4e4e4;
  }
  *{box-sizing:border-box;margin:0;padding:0}
  html,body{width:1200px;height:1200px;overflow:hidden;background:var(--stage);font-family:"Roboto",sans-serif;color:var(--ink)}
  .sheet{position:relative;width:1200px;height:1200px}
  .card{position:absolute;left:180px;width:840px;height:560px;background:var(--paper);overflow:hidden;box-shadow:0 6px 18px rgba(0,0,0,.18)}
  .card--back{top:30px}
  .card--front{top:610px}
  .abs{position:absolute}
  .shapes{position:absolute;inset:0;width:100%;height:100%}
  .brand{display:flex;align-items:center;gap:8px;font-family:"Roboto Condensed",sans-serif;font-weight:700;font-size:24px;color:var(--dark)}
  .brand__mark{width:20px;height:20px;background:var(--blue)}
  .tick{display:inline-block;width:15px;height:15px;flex:none;margin-right:10px;margin-top:2px}
  .ticks{list-style:none}
  .ticks li{display:flex;align-items:flex-start}

  /* FRONT */
  .front__logo{right:40px;top:36px}
  .front__hook{left:40px;top:44px;font-family:"Roboto Condensed",sans-serif;font-weight:700;color:var(--orange);font-size:23px}
  .front__say{left:110px;top:78px;font-family:"Roboto Condensed",sans-serif;font-size:20px;color:var(--dark);padding-bottom:4px;border-bottom:2px solid var(--blue);padding-right:40px}
  .front__quote{left:28px;top:120px;font-family:"Oswald",sans-serif;font-weight:500;font-size:25px;line-height:1.12;color:var(--blue);text-transform:uppercase}
  .front__quote .q{color:var(--orange);font-size:34px;vertical-align:-6px}
  .front__quote .l2{padding-left:22px}
  .front__band{left:0;top:258px;width:760px;height:216px;background:var(--dark);border-top:4px solid var(--orange);border-bottom:4px solid var(--orange)}
  .front__list{left:30px;top:274px;width:410px;color:#fff;font-size:13.5px;line-height:1.3}
  .front__list li{margin-bottom:6px}
  .front__web{left:40px;top:512px;display:flex;align-items:center;gap:10px;font-size:14px}
  .front__phone{left:300px;top:512px;display:flex;align-items:center;gap:10px;font-size:14px}

  /* BACK */
  .back__title{left:30px;top:34px;font-weight:700;font-size:18px;color:var(--blue);text-transform:uppercase}
  .back__title span{color:var(--orange);font-weight:500}
  .back__intro{left:30px;top:62px;width:400px;font-size:12.5px;line-height:1.35}
  .back__intro b{color:var(--orange);font-weight:500}
  .back__bandtext{left:30px;top:137px;width:440px;color:#fff;font-weight:500;font-size:13px;line-height:1.35;text-transform:uppercase}
  .back__list{left:30px;top:214px;font-size:15px;font-weight:500;line-height:1.3}
  .back__list li{margin-bottom:9px}
  .back__list .fig{color:var(--blue);font-weight:700;margin-right:4px}
  .back__logo{left:120px;top:484px}
  .back__note{left:590px;top:28px;width:230px;font-size:11.5px;line-height:1.3}
  .back__note b{color:var(--blue);font-weight:500}
  .back__form{left:590px;top:94px;width:230px;font-size:12px;color:var(--blue);font-weight:500}
  .field{display:flex;align-items:flex-end;height:22px}
  .field span.line{flex:1;border-bottom:1.5px dotted var(--ink);margin-left:4px;margin-bottom:3px}
  .back__ctatext{left:590px;top:212px;width:232px;color:#fff;font-size:11.5px;line-height:1.35}
  .back__ctatext b{color:var(--blue);font-weight:700;text-transform:uppercase}
  .back__ctatext b em{font-style:normal;color:#fff}
</style>
</head>
<body>
<main class="sheet">

  <!-- BACK SIDE -->
  <section class="card card--back" aria-label="Postcard back">
    <svg class="shapes" viewBox="0 0 840 560">
      <defs>
        <linearGradient id="faintTone" x1="0" y1="0" x2="1" y2="1">
          <stop offset="0" stop-color="#fafafa"/><stop offset=".6" stop-color="#ececec"/><stop offset="1" stop-color="#f6f6f6"/>
        </linearGradient>
        <linearGradient id="appTone" x1="0" y1="0" x2="1" y2="1">
          <stop offset="0" stop-color="#eef2f6"/><stop offset="1" stop-color="#cfd9e4"/>
        </linearGradient>
        <clipPath id="panelClip"><path d="M460 0 C 580 160 590 400 480 560 L840 560 L840 0 Z"/></clipPath>
      </defs>
      <rect x="0" y="0" width="620" height="560" fill="url(#faintTone)" role="img" aria-label="Faint background photo of smiling medical staff"/>
      <rect x="0" y="128" width="620" height="62" fill="#2b2b2b"/>
      <g clip-path="url(#panelClip)">
        <rect x="400" y="0" width="440" height="560" fill="#f6f6f6"/>
        <rect x="400" y="202" width="440" height="96" fill="#2b2b2b"/>
        <rect x="400" y="298" width="440" height="262" fill="url(#appTone)" role="img" aria-label="Three smartphones showing the claims app screens"/>
      </g>
      <path d="M450 0 C 570 160 580 400 470 560" fill="none" stroke="#f7941d" stroke-width="7"/>
      <path d="M460 0 C 580 160 590 400 480 560" fill="none" stroke="#1a73c2" stroke-width="9"/>
    </svg>

    <div class="abs back__title">How this saves <span>you money</span></div>
    <p class="abs back__intro">Assuming a <b>38%</b> personal tax rate. You will need to earn <b>$1.62</b> of gross income, pay <b>$0.62</b> of personal tax, which leaves you with <b>$1.00</b> of after tax money to use for your personal expenses.</p>
    <p class="abs back__bandtext">The example of using a 789 Brookvale Outlay Plan, or doing nothing would need the following information.</p>

    <ul class="abs ticks back__list">
      <li><svg class="tick" viewBox="0 0 16 16"><circle cx="8" cy="8" r="6.5" fill="none" stroke="#f7941d" stroke-width="1.6"/><path d="M4.8 8.2l2.2 2.2 4-4.4" fill="none" stroke="#f7941d" stroke-width="1.8"/></svg>Comparison</li>
      <li><svg class="tick" viewBox="0 0 16 16"><circle cx="8" cy="8" r="6.5" fill="none" stroke="#f7941d" stroke-width="1.6"/><path d="M4.8 8.2l2.2 2.2 4-4.4" fill="none" stroke="#f7941d" stroke-width="1.8"/></svg><span><span class="fig">$5,000</span>Of Medical, Dental, Vision Expenses</span></li>
      <li><svg class="tick" viewBox="0 0 16 16"><circle cx="8" cy="8" r="6.5" fill="none" stroke="#f7941d" stroke-width="1.6"/><path d="M4.8 8.2l2.2 2.2 4-4.4" fill="none" stroke="#f7941d" stroke-width="1.8"/></svg>Do Nothing 789 Brookvale Outlay Plan</li>
      <li><svg class="tick" viewBox="0 0 16 16"><circle cx="8" cy="8" r="6.5" fill="none" stroke="#f7941d" stroke-width="1.6"/><path d="M4.8 8.2l2.2 2.2 4-4.4" fill="none" stroke="#f7941d" stroke-width="1.8"/></svg><span><span class="fig">$8,100</span>– Total Cost &nbsp;<span class="fig">$5,525</span>– Total Cost</span></li>
      <li><svg class="tick" viewBox="0 0 16 16"><circle cx="8" cy="8" r="6.5" fill="none" stroke="#f7941d" stroke-width="1.6"/><path d="M4.8 8.2l2.2 2.2 4-4.4" fill="none" stroke="#f7941d" stroke-width="1.8"/></svg><span><span class="fig">$3,100</span>– Income Tax &nbsp;<span class="fig">$500</span>Fee &amp; <span class="fig">$25</span>Gst</span></li>
      <li><svg class="tick" viewBox="0 0 16 16"><circle cx="8" cy="8" r="6.5" fill="none" stroke="#f7941d" stroke-width="1.6"/><path d="M4.8 8.2l2.2 2.2 4-4.4" fill="none" stroke="#f7941d" stroke-width="1.8"/></svg><span><span class="fig">$5,000</span>– Money Needed For Medical, Dental, Vision, Etc</span></li>
    </ul>
    <div class="abs brand back__logo"><span class="brand__mark"></span>789 Brookvale</div>

    <p class="abs back__note">Assuming a company incorporated in Alberta and a one time setup fee of <b>$275</b> has not been included in the comparison.</p>
    <div class="abs back__form">
      <div class="field">Names:<span class="line"></span></div>
      <div class="field">DOB:<span class="line"></span></div>
      <div class="field">Address:<span class="line"></span>&nbsp;Phone:<span class="line"></span></div>
      <div class="field">e-mail:<span class="line"></span></div>
    </div>
    <p class="abs back__ctatext">We will contact you about how to setup the app, your banking details and some other items.<br><b>Setup fee is a one-time payment of <em>$275</em></b></p>
  </section>

  <!-- FRONT SIDE -->
  <section class="card card--front" aria-label="Postcard front">
    <div class="front__band abs"></div>
    <svg class="shapes" viewBox="0 0 840 560">
      <defs>
        <linearGradient id="photoTone" x1="0" y1="0" x2="1" y2="1">
          <stop offset="0" stop-color="#efe4d6"/>
          <stop offset=".55" stop-color="#d9c8b4"/>
          <stop offset="1" stop-color="#b9a896"/>
        </linearGradient>
      </defs>
      <path d="M484 0 C 404 180 444 420 684 560" fill="none" stroke="#1a73c2" stroke-width="8"/>
      <path d="M500 0 C 420 180 460 420 700 560 L840 560 L840 0 Z" fill="url(#photoTone)" stroke="#fff" stroke-width="12" role="img" aria-label="Photo of a smiling medical team looking at a tablet"/>
    </svg>
    <div class="abs brand front__logo"><span class="brand__mark"></span>789 Brookvale</div>

    <div class="abs front__hook">You're Spending Too Much On Taxes!</div>
    <div class="abs front__say">That's What They'll Say</div>
    <h1 class="abs front__quote"><span class="q">&ldquo;</span> If your business doesn't have a<br><span class="l2">789 Brookvale Outlay Plan... <span class="q">&rdquo;</span></span></h1>

    <ul class="abs ticks front__list">
      <li><svg class="tick" viewBox="0 0 16 16"><circle cx="8" cy="8" r="6.5" fill="none" stroke="#f7941d" stroke-width="1.6"/><path d="M4.8 8.2l2.2 2.2 4-4.4" fill="none" stroke="#f7941d" stroke-width="1.8"/></svg>Who Should Have a 789 Brookvale Outlay Plan?</li>
      <li><svg class="tick" viewBox="0 0 16 16"><circle cx="8" cy="8" r="6.5" fill="none" stroke="#f7941d" stroke-width="1.6"/><path d="M4.8 8.2l2.2 2.2 4-4.4" fill="none" stroke="#f7941d" stroke-width="1.8"/></svg>Every Business Owner Who is Incorporated Should Have One.</li>
      <li><svg class="tick" viewBox="0 0 16 16"><circle cx="8" cy="8" r="6.5" fill="none" stroke="#f7941d" stroke-width="1.6"/><path d="M4.8 8.2l2.2 2.2 4-4.4" fill="none" stroke="#f7941d" stroke-width="1.8"/></svg>Write off 100% of This QTB Approved This Method</li>
      <li><svg class="tick" viewBox="0 0 16 16"><circle cx="8" cy="8" r="6.5" fill="none" stroke="#f7941d" stroke-width="1.6"/><path d="M4.8 8.2l2.2 2.2 4-4.4" fill="none" stroke="#f7941d" stroke-width="1.8"/></svg>It Is The Most Tax Effective Way To Run Dental, Health, Vision &amp; Other Expenses Through Your Company.</li>
      <li><svg class="tick" viewBox="0 0 16 16"><circle cx="8" cy="8" r="6.5" fill="none" stroke="#f7941d" stroke-width="1.6"/><path d="M4.8 8.2l2.2 2.2 4-4.4" fill="none" stroke="#f7941d" stroke-width="1.8"/></svg>Easy To Use App For Your Phone, 2-day Turnaround Time For Claims</li>
      <li><svg class="tick" viewBox="0 0 16 16"><circle cx="8" cy="8" r="6.5" fill="none" stroke="#f7941d" stroke-width="1.6"/><path d="M4.8 8.2l2.2 2.2 4-4.4" fill="none" stroke="#f7941d" stroke-width="1.8"/></svg>If you aren't using this, you're throwing tax dollars away!</li>
    </ul>

    <div class="abs front__web">
      <svg width="20" height="20" viewBox="0 0 20 20" aria-hidden="true"><circle cx="10" cy="10" r="9" fill="#1a73c2"/><path d="M1 10h18M10 1c-4 4-4 14 0 18M10 1c4 4 4 14 0 18" fill="none" stroke="#fff" stroke-width="1.2"/></svg>
      www.brookvaleplan.ca
    </div>
    <div class="abs front__phone">
      <svg width="22" height="20" viewBox="0 0 24 24" aria-hidden="true"><path d="M6.6 10.8a15 15 0 006.6 6.6l2.2-2.2a1 1 0 011-.25 11.4 11.4 0 003.6.57 1 1 0 011 1V20a1 1 0 01-1 1A17 17 0 013 4a1 1 0 011-1h3.5a1 1 0 011 1c0 1.25.2 2.45.57 3.6a1 1 0 01-.25 1z" fill="#1a73c2"/></svg>
      (587) 555 0148
    </div>
  </section>

</main>
</body>
</html>
```